Zielgruppe
Friseurin für Damen und Herren
Aufgabenstellung
https://lumiraschnitt.de
Bitte erstelle mir anhand der Daten von der Website einen angepassten Entwurf mit Neueröffnung und geben keine Preise an sondern die kunden sollen sich direkt eingeladen führen um persönlich vor Ort vorbei zuschauen.

```html
<!DOCTYPE html>
<html lang="de">
<head>
<meta charset="utf-8">
<title>Lumira Hair &amp; Beautylounge – Neueröffnung</title>
<link href="https://fonts.googleapis.com/css2?family=Inter:wght@300;400;500;700;800&display=swap" rel="stylesheet">
<style>
  :root {
    --sage: #6d7c5f;
    --sage-dark: #3f4a38;
    --blush: #e8b4a2;
    --ink: #161616;
    --white: #ffffff;
    --text-dark: #1f1d1c;
    --text-soft: #3a3331;
  }
  html, body { margin: 0; padding: 0; overflow: hidden; }
  body { width: 846px; height: 1200px; background: var(--sage); font-family: "Inter", Arial, sans-serif; }
  .flyer { position: relative; width: 846px; height: 1200px; overflow: hidden; }
  .flyer__shapes { position: absolute; inset: 0; }

  .headline {
    position: absolute; left: 47px; top: 24px; margin: 0;
    color: var(--white); font-weight: 400; font-size: 55px; line-height: 51.5px; letter-spacing: 0.3px;
  }
  .headline strong { font-weight: 800; }

  .tagline {
    position: absolute; left: 363px; top: 618px; margin: 0;
    color: var(--text-dark); font-size: 32.5px; line-height: 34px; font-weight: 400; letter-spacing: 1.3px;
    white-space: nowrap;
  }
  .tagline strong { font-weight: 800; }

  .intro {
    position: absolute; right: 57px; top: 740px; margin: 0; width: 440px;
    text-align: right; color: var(--text-soft); font-size: 15.6px; line-height: 19.6px; font-weight: 300;
    letter-spacing: 0.3px;
  }
  .intro strong { font-weight: 500; }

  .address {
    position: absolute; right: 57px; top: 968px; margin: 0;
    text-align: right; color: var(--text-dark); font-weight: 800; font-size: 20.5px; line-height: 24px; font-style: normal;
  }
  .address__zip { display: block; margin-top: 32px; }

  .hours {
    position: absolute; right: 57px; top: 1082px; margin: 0;
    text-align: right; color: var(--text-dark); font-size: 15.2px; line-height: 18.6px; font-weight: 700;
    white-space: nowrap;
  }
  .hours__title { display: block; }

  .brand {
    position: absolute; left: 96px; top: 1008px; width: 300px; text-align: center; color: var(--white);
  }
  .brand__name { margin: 0; font-size: 50px; line-height: 52px; font-weight: 700; letter-spacing: 1px; }
  .brand__sub { margin: 4px 0 0; font-size: 18.2px; line-height: 21px; font-weight: 400; letter-spacing: 0.4px; white-space: nowrap; }

  .contact { position: absolute; left: 140px; top: 1096px; color: var(--white); }
  .contact__icon { position: absolute; left: 0; top: 5px; width: 34px; height: 34px; }
  .contact__numbers { margin: 0 0 0 47px; font-size: 17.6px; line-height: 21px; font-weight: 700; letter-spacing: 0.5px; white-space: nowrap; }
  .contact__web { position: absolute; left: 47px; top: 53px; font-size: 12px; font-weight: 400; white-space: nowrap; }
</style>
</head>
<body>
<main class="flyer">
  <svg class="flyer__shapes" width="846" height="1200" viewBox="0 0 846 1200">
    <defs>
      <linearGradient id="bgShade" x1="0" y1="0" x2="1" y2="1">
        <stop offset="0" stop-color="#3e4837"/>
        <stop offset="0.55" stop-color="#6d7c5f"/>
      </linearGradient>
      <radialGradient id="blondeTone" cx="0.55" cy="0.35" r="0.6">
        <stop offset="0" stop-color="#e6cfa8"/>
        <stop offset="0.5" stop-color="#c99a86"/>
        <stop offset="1" stop-color="#6d7c5f" stop-opacity="0"/>
      </radialGradient>
      <radialGradient id="darkTone" cx="0.7" cy="0.5" r="0.7">
        <stop offset="0" stop-color="#d9a392"/>
        <stop offset="0.45" stop-color="#4a3a38"/>
        <stop offset="1" stop-color="#0f0f10"/>
      </radialGradient>
      <radialGradient id="copperTone" cx="0.5" cy="0.5" r="0.6">
        <stop offset="0" stop-color="#e8c3ad"/>
        <stop offset="0.55" stop-color="#c0612f"/>
        <stop offset="1" stop-color="#6b3420"/>
      </radialGradient>
    </defs>

    <rect class="bg" width="846" height="1200" fill="url(#bgShade)"/>

    <g role="img" aria-label="Foto: Frau im Profil mit blonder Hochsteckfrisur und roten Strähnen">
      <ellipse cx="610" cy="300" rx="330" ry="360" fill="url(#blondeTone)"/>
    </g>

    <path class="shape-blush" d="M0,220 C150,230 290,320 380,470 C440,560 560,590 846,632 L846,1200 L0,1200 Z" fill="var(--blush)"/>

    <circle class="ring-blush" cx="131" cy="489" r="240" fill="var(--blush)"/>
    <g role="img" aria-label="Foto: Frau mit schwarzem Bob, Pony und pinkem Make-up im Profil">
      <circle cx="131" cy="489" r="217" fill="url(#darkTone)"/>
    </g>

    <path class="shape-sage-border" d="M0,712 C90,712 150,690 210,660 L372,706 C450,790 505,950 512,1200 L0,1200 Z" fill="var(--sage)"/>
    <path class="shape-ink" d="M0,724 C90,724 150,702 210,672 L362,720 C436,800 490,955 495,1200 L0,1200 Z" fill="var(--ink)"/>

    <circle class="ring-sage" cx="243" cy="790" r="128" fill="var(--sage)"/>
    <g role="img" aria-label="Foto: Frau mit langen kupferroten Wellen und Ohrring">
      <circle cx="243" cy="790" r="118" fill="url(#copperTone)"/>
    </g>

    <circle class="dot-sage" cx="21" cy="1062" r="71" fill="var(--sage)"/>
  </svg>

  <h1 class="headline">Unsere <strong>Experten</strong><br>verwandeln<br>Ihre <strong>Träume</strong><br>in <strong>Realität</strong>.</h1>

  <h2 class="tagline">ERLEBEN SIE<br><strong>SCHÖNHEIT</strong> UND <strong>STIL</strong><br>IN PERFEKTER <strong>HARMONIE</strong>.</h2>

  <p class="intro"><strong>Neueröffnung</strong> unseres Salons in Großaitingen!<br>Wir laden Sie herzlich ein, uns persönlich<br>vor Ort zu besuchen und kennenzulernen.<br>Unser erfahrenes Team sorgt dafür,<br>dass Sie sich rundum wohlfühlen.</p>

  <address class="address">Großaitingen<br>Ahornweg 7<span class="address__zip">86845 Großaitingen</span></address>

  <p class="hours"><span class="hours__title">Geschäftszeiten:</span>Di. - Do. 09:00 Uhr bis 18:00 Uhr<br>Fr. 09:00 - 20:00 Uhr<br>Sa. 09:00 - 14:00 Uhr</p>

  <div class="brand">
    <p class="brand__name">LUMIRA</p>
    <p class="brand__sub">HAIR &amp; BEAUTYLOUNGE</p>
  </div>

  <div class="contact">
    <svg class="contact__icon" viewBox="0 0 34 34" aria-hidden="true">
      <circle cx="17" cy="17" r="17" fill="var(--white)"/>
      <path d="M11.5 9.5c1-.6 2-.4 2.6.6l1.4 2.4c.5.9.3 1.9-.5 2.5l-1 .8c.9 2 2.4 3.6 4.4 4.6l.9-1c.6-.8 1.7-.9 2.5-.4l2.3 1.5c.9.6 1.1 1.7.5 2.6-1 1.6-2.9 2.3-4.7 1.700-4.9-1.700-8.400-5.400-9.900-10.300-.5-1.800.3-3.700 1.500-4.900z" fill="var(--ink)"/>
      <path d="M19 9.5a6 6 0 0 1 5.5 5.5M19 12.5a3 3 0 0 1 2.5 2.5" stroke="var(--ink)" stroke-width="1.5" fill="none" stroke-linecap="round"/>
    </svg>
    <p class="contact__numbers">0821-4 57 12 88 0<br>0152-300 414 27</p>
    <span class="contact__web">www.lumiraschnitt.de</span>
  </div>
</main>
</body>
</html>
```